New Web Design Project open cart

We are about to start a new furniture selling website and it will be based on open cart . we mainly need two pages designing landing page & item page. so come up with your unique ideas and designs . Please make sure the design needs to be unique . no templates and themes . Will make the selected designer even happier if your design is selected. So basically over all it is going to be the new theme for our open cart base eCommerce website .we will appreciate if its responsive with some unique features .
SO as per request of designers about more brief about the project = WE ONLY NEED A RESPONSIVE THEME FOR OUR OPEN CART BASE eCommerce WebSite . Mainly item page & product page needs a good unique design. Lighter, speed load, compatible with all browsers and responsive will be appreciated . To Get an idea check on loungerix .co .uk website or tablowmeadows etc.
more projects coming soon .

Our audience will be furniture buying customers .

Furniture

• to get some sort of idea have a look at loungerix .co uk`s website`s listing page and landing page .
• responsive, easy to customize, full theme .

```html
<!DOCTYPE html>
<html lang="en">
<head>
<meta charset="utf-8">
<title>Oakmere Home – Furniture Store</title>
<link rel="stylesheet" href="https://fonts.googleapis.com/css2?family=Lato:wght@400;700&family=Oswald:wght@400;500&family=Kaushan+Script&display=swap">
<style>
:root{
  --pink:#e8265f;
  --pink-dark:#c81e4f;
  --teal:#1c9aab;
  --teal-light:#22aebf;
  --orange:#f7941d;
  --green:#8cb43c;
  --green-dark:#79a02e;
  --ink:#333;
  --muted:#555;
  --line:#e2e2e2;
  --beige:#f1ece2;
  --footer:#2c2c2c;
  --footer-text:#ddd;
}
*{box-sizing:border-box;margin:0;padding:0}
html,body{width:726px;height:1200px;overflow:hidden;background:#fff}
body{position:relative;font-family:'Lato',sans-serif;color:var(--ink);font-size:9px}
.abs{position:absolute}

/* header */
.account-bar{left:526px;top:0;display:flex;height:22px}
.account-bar a{background:var(--green);color:#fff;text-decoration:none;font-size:8px;display:flex;align-items:center;gap:5px;padding:0 10px;border-right:1px solid var(--green-dark)}
.account-bar a:first-child{border-radius:0 0 0 3px}
.account-bar a:last-child{border-radius:0 0 3px 0;border:0}
.user-links{left:432px;top:36px;display:flex;gap:10px;font-size:8px;color:var(--muted)}
.user-links span{display:flex;align-items:center;gap:5px}
.user-links i{width:1px;height:10px;background:#ccc}
.search{left:371px;top:61px;width:175px;height:22px;border:1px solid #ccc;font-size:7px;color:#888;padding:7px 8px}
.search svg{position:absolute;right:6px;top:5px}
.cart{left:552px;top:61px;width:94px;height:22px;border:1px solid #ccc;font-size:8px;font-weight:700;display:flex;align-items:center;gap:5px;padding-left:8px}

.logo{left:79px;top:12px;display:flex;align-items:center;gap:8px}
.logo-square{width:60px;height:60px;border-radius:6px;background:var(--pink)}
.logo-name{font-size:25px;font-weight:700;color:var(--ink);line-height:1}

/* nav */
.main-nav{left:0;top:94px;width:726px;height:28px;background:var(--pink);border-top:2px solid var(--pink-dark)}
.main-nav ul{list-style:none;display:flex;position:absolute;left:79px;top:0;height:26px}
.main-nav li{color:#fff;font-size:9px;padding:0 19px;display:flex;align-items:center;border-right:1px solid rgba(255,255,255,.3)}
.main-nav li:last-child{border:0}
.main-nav li.active{background:var(--teal);padding:0 18px}

/* hero */
.hero{left:0;top:122px;width:726px;height:238px;background:linear-gradient(100deg,#d9d7d0 0%,#a89376 35%,#7a5232 60%,#9a6a45 80%,#c8b8a0 100%)}
.hero-title{left:150px;top:238px;font-family:'Kaushan Script',cursive;color:#fff;font-size:20px;line-height:28px;text-shadow:0 2px 3px rgba(0,0,0,.45)}
.hero-title span{display:block;padding-left:30px}
.dots{left:607px;top:344px;display:flex;gap:5px}
.dots i{width:9px;height:9px;border-radius:50%;background:#fff}
.dots i:first-child{background:var(--pink)}

/* quick categories */
.quick-cats{left:0;top:360px;width:726px;height:68px;background:var(--beige)}
.quick-item{position:absolute;top:14px;display:flex;align-items:center;gap:9px;font-size:12px;color:var(--ink)}
.quick-icon{width:40px;height:40px;border-radius:7px;display:flex;align-items:center;justify-content:center}
.quick-sep{position:absolute;top:12px;width:1px;height:44px;background:#ddd5c6}

/* promos */
.promo{top:445px;width:182px;height:102px;border:3px solid #e6e0d2}
.promo-save{left:79px}
.promo-ship{left:272px;background:var(--pink);border-color:#f0c5d2;color:#fff;text-align:center}
.promo-ship .inner{position:absolute;inset:4px;border:1px dashed rgba(255,255,255,.7)}
.promo-offer{left:465px}
.promo-photo{position:absolute;border-radius:4px}

/* section labels */
.label{height:22px;display:flex;align-items:center;color:#fff;font-size:11px;padding:0 16px 0 8px;clip-path:polygon(0 0,88% 0,100% 100%,0 100%)}
.label-rule{height:5px;background:repeating-linear-gradient(45deg,#e8e8e8 0 2px,#f6f6f6 2px 4px)}
.divider{left:79px;width:567px;height:5px;background:repeating-linear-gradient(45deg,#e4e4e4 0 2px,#f6f6f6 2px 4px)}

/* product cards */
.product{top:601px;width:133px;height:171px;border:1px solid var(--line)}
.product .photo{position:absolute;left:10px;top:6px;width:111px;height:86px;border-radius:3px}
.price{position:absolute;left:8px;top:104px;font-size:10px;color:var(--ink)}
.product-name{position:absolute;left:6px;top:124px;font-size:8.5px;font-weight:700}
.btn-cart{position:absolute;left:6px;top:145px;width:80px;height:20px;background:var(--teal);color:#fff;font-size:7.5px;font-weight:700;display:flex;align-items:center;gap:5px;padding-left:6px}

/* category cards */
.category{top:839px;width:133px;height:149px;border:1px solid var(--line)}
.category .photo{position:absolute;left:2px;top:2px;width:128px;height:92px}
.category h3{position:absolute;left:6px;top:100px;font-size:11.5px;font-weight:400}
.btn-more{position:absolute;left:6px;top:124px;height:18px;padding:0 8px;background:var(--teal);color:#fff;font-size:7.5px;font-weight:700;display:flex;align-items:center;gap:4px}

/* brand strip */
.brands{left:79px;top:1024px;width:567px;display:flex;justify-content:space-between;align-items:center;font-size:11px;font-weight:700;color:#333}

/* footer */
.footer{left:0;top:1061px;width:726px;height:116px;background:var(--footer);color:var(--footer-text)}
.fcol{position:absolute;top:12px}
.fcol h4{font-size:11.5px;font-weight:400;color:#fff;padding-bottom:5px;border-bottom:1px solid #444;margin-bottom:6px}
.fcol li{list-style:none;font-size:7.5px;line-height:18px}
.fcol li::before{content:"› "}
.fcol p{font-size:7.5px;line-height:11px}
.email{width:117px;height:16px;background:#fff;color:#888;font-size:6.5px;padding:4px 6px;margin-top:7px}
.btn-sub{display:inline-block;margin-top:7px;background:#aaa;color:#222;font-size:7.5px;font-weight:700;padding:4px 7px}
.social li{display:flex;align-items:center;gap:7px;line-height:21px}
.social li::before{content:none}
.social b{width:13px;height:13px;background:#fff;display:inline-block}
.bottom-bar{left:0;top:1177px;width:726px;height:23px;background:var(--pink);color:#fff;font-size:7.5px}
.bottom-bar .copy{position:absolute;left:81px;top:7px}
.pay{position:absolute;top:5px;right:79px;display:flex;gap:3px}
.pay span{background:#fff;color:var(--ink);font-size:5.5px;font-weight:700;width:24px;height:13px;display:flex;align-items:center;justify-content:center}
</style>
</head>
<body>

<header>
  <nav class="account-bar abs">
    <a href="#"><svg width="7" height="8" viewBox="0 0 7 8"><rect x="0" y="3.5" width="7" height="4.5" fill="#fff"/><path d="M1.5 3.5V2a2 2 0 0 1 4 0v1.5" stroke="#fff" fill="none"/></svg>Login</a>
    <a href="#"><svg width="8" height="8" viewBox="0 0 8 8"><rect x=".5" y=".5" width="6" height="7" fill="none" stroke="#fff"/><path d="M2 3h3M2 5h2" stroke="#fff"/></svg>Register</a>
  </nav>
  <div class="user-links abs">
    <span><svg width="8" height="9" viewBox="0 0 8 9"><circle cx="4" cy="2.5" r="2.2" fill="#666"/><path d="M0 9a4 4 0 0 1 8 0z" fill="#666"/></svg>My Account</span><i></i>
    <span><svg width="9" height="8" viewBox="0 0 9 8"><path d="M4.5 7.5 1 4A2 2 0 0 1 4.5 1.2 2 2 0 0 1 8 4z" fill="none" stroke="#666"/></svg>My Wishlist</span><i></i>
    <span><svg width="11" height="8" viewBox="0 0 11 8"><path d="M0 .5h2l1.5 5h6l1-4H3" fill="none" stroke="#666"/><circle cx="4" cy="7.2" r=".8" fill="#666"/><circle cx="9" cy="7.2" r=".8" fill="#666"/></svg>Checkout</span>
  </div>
  <div class="search abs">Search
    <svg width="10" height="10" viewBox="0 0 10 10"><circle cx="4" cy="4" r="3.2" fill="none" stroke="#666" stroke-width="1.2"/><path d="M6.5 6.5 9.5 9.5" stroke="#666" stroke-width="1.4"/></svg>
  </div>
  <div class="cart abs">
    <svg width="11" height="9" viewBox="0 0 11 9"><path d="M0 3h11l-1.5 6h-8z" fill="#555"/><path d="M3 3 5 0M8 3 6 0" stroke="#555"/></svg>Shopping Cart
    <svg width="7" height="5" viewBox="0 0 7 5"><path d="M.5.5 3.5 3.5 6.5.5" fill="none" stroke="#333" stroke-width="1.3"/></svg>
  </div>
  <div class="logo abs">
    <div class="logo-square"></div>
    <div class="logo-name">Oakmere<br>Home</div>
  </div>
</header>

<nav class="main-nav abs">
  <ul>
    <li class="active">HOME</li><li>BEDROOM</li><li>LIVING ROOM</li><li>DINING ROOM</li><li>KIDS ROOMS</li><li>BRANDS</li><li>SALE</li>
  </ul>
</nav>

<section>
  <div class="hero abs" role="img" aria-label="Wooden dining table and chairs on a sunny terrace beside a brick wall"></div>
  <h1 class="hero-title abs">Make it Your<span>Dream Home</span></h1>
  <div class="dots abs"><i></i><i></i><i></i></div>
</section>

<section class="quick-cats abs">
  <div class="quick-item" style="left:113px">
    <div class="quick-icon" style="background:var(--pink)"><svg width="22" height="16" viewBox="0 0 22 16"><rect x="3" y="2" width="16" height="8" rx="2" fill="none" stroke="#fff" stroke-width="2"/><rect x="1" y="6" width="20" height="7" rx="2" fill="#fff"/><path d="M3 13v3M19 13v3" stroke="#fff" stroke-width="2"/></svg></div>Sofas</div>
  <div class="quick-sep" style="left:222px"></div>
  <div class="quick-item" style="left:252px">
    <div class="quick-icon" style="background:var(--orange)"><svg width="22" height="18" viewBox="0 0 22 18"><path d="M1 2h10M6 2v16M13 2v16M13 8h8M21 8v10M13 13h8" stroke="#fff" stroke-width="2" fill="none"/></svg></div>Dining</div>
  <div class="quick-sep" style="left:363px"></div>
  <div class="quick-item" style="left:385px">
    <div class="quick-icon" style="background:var(--green)"><svg width="16" height="22" viewBox="0 0 16 22"><rect x="1" y="1" width="14" height="19" fill="none" stroke="#fff" stroke-width="2"/><path d="M8 1v19M6 10v2M10 10v2" stroke="#fff" stroke-width="1.5"/></svg></div>Cupboard</div>
  <div class="quick-sep" style="left:505px"></div>
  <div class="quick-item" style="left:538px">
    <div class="quick-icon" style="background:var(--teal-light)"><svg width="18" height="20" viewBox="0 0 18 20"><path d="M9 1 17 10H1z" fill="#fff"/><rect x="6" y="10" width="6" height="6" fill="#fff"/><rect x="4" y="17" width="10" height="2" fill="#fff"/></svg></div>Lamp</div>
</section>

<section>
  <div class="promo promo-save abs">
    <div class="abs" style="left:11px;top:12px;color:var(--teal);font-size:24px">Save</div>
    <div class="abs" style="left:28px;top:37px;color:#888;font-size:15px">up to</div>
    <div class="abs" style="left:11px;top:56px;color:var(--pink);font-size:24px">50%<span style="font-size:14px;color:#888">off</span></div>
    <div class="promo-photo" style="left:100px;top:10px;width:72px;height:78px;background:radial-gradient(circle,#e8ddc8,#cbb48e 60%,#fff 72%)" role="img" aria-label="Round woven daybed with white cushions"></div>
  </div>
  <div class="promo promo-ship abs">
    <div class="inner"></div>
    <div class="abs" style="left:0;right:0;top:18px;font-family:'Oswald',sans-serif;font-size:25px;line-height:1">FREE SHIPPING</div>
    <svg class="abs" style="left:84px;top:54px" width="10" height="10" viewBox="0 0 10 10"><path d="M5 0 6.2 3.6H10L7 5.8 8.1 9.5 5 7.2 1.9 9.5 3 5.8 0 3.6H3.8z" fill="#fff"/></svg>
    <div class="abs" style="left:0;right:0;top:70px;font-size:14px">on orders over $ 999</div>
  </div>
  <div class="promo promo-offer abs">
    <div class="promo-photo" style="left:8px;top:14px;width:90px;height:74px;background:radial-gradient(ellipse,#5a3a2a,#3a2418 45%,#fff 72%)" role="img" aria-label="Dark wooden dining set with red table runner"></div>
    <div class="abs" style="right:11px;top:12px;color:#999;font-size:14px">Special</div>
    <div class="abs" style="right:11px;top:32px;color:var(--orange);font-size:22px">OFFER</div>
    <div class="abs" style="right:17px;top:60px;color:var(--pink);font-size:24px">15%<span style="font-size:14px;color:#999">off</span></div>
  </div>
</section>

<section>
  <div class="abs" style="left:79px;top:567px;width:567px;display:flex;align-items:flex-end">
    <div class="label" style="background:var(--orange);width:99px">BEST SELLERS</div>
    <div class="label-rule" style="flex:1;margin-bottom:0"></div>
  </div>
  <article class="product abs" style="left:79px"><div class="photo" style="background:radial-gradient(ellipse,#c9b39a,#8a6a4a 50%,#fff 72%)" role="img" aria-label="Upholstered bed with wooden storage drawers"></div><div class="price">$199.00</div><div class="product-name">Lorem ipsum dolor sit amet</div><div class="btn-cart"><svg width="10" height="8" viewBox="0 0 11 9"><path d="M0 3h11l-1.5 6h-8z" fill="#fff"/></svg>ADD TO CART</div></article>
  <article class="product abs" style="left:224px"><div class="photo" style="background:radial-gradient(ellipse,#c89a6a,#7a3a1e 40%,#fff 65%)" role="img" aria-label="Carved wooden dining chair"></div><div class="price">$100.95</div><div class="product-name">Lorem ipsum dolor sit amet</div><div class="btn-cart"><svg width="10" height="8" viewBox="0 0 11 9"><path d="M0 3h11l-1.5 6h-8z" fill="#fff"/></svg>ADD TO CART</div></article>
  <article class="product abs" style="left:368px"><div class="photo" style="background:radial-gradient(ellipse,#5a3a28,#3b2418 50%,#fff 72%)" role="img" aria-label="Brown corner sofa with ottoman"></div><div class="price">$100.95</div><div class="product-name">Lorem ipsum dolor sit amet</div><div class="btn-cart"><svg width="10" height="8" viewBox="0 0 11 9"><path d="M0 3h11l-1.5 6h-8z" fill="#fff"/></svg>ADD TO CART</div></article>
  <article class="product abs" style="left:513px"><div class="photo" style="background:radial-gradient(ellipse,#4a3a30,#2a1e18 45%,#fff 70%)" role="img" aria-label="Dark dining table with four chairs"></div><div class="price">$100.95</div><div class="product-name">Lorem ipsum dolor sit amet</div><div class="btn-cart"><svg width="10" height="8" viewBox="0 0 11 9"><path d="M0 3h11l-1.5 6h-8z" fill="#fff"/></svg>ADD TO CART</div></article>
</section>

<div class="divider abs" style="top:785px"></div>

<section>
  <div class="abs" style="left:79px;top:806px;width:567px;display:flex;align-items:flex-end">
    <div class="label" style="background:var(--green);width:95px">CATEGORIES</div>
    <div class="label-rule" style="flex:1"></div>
  </div>
  <article class="category abs" style="left:79px"><div class="photo" style="background:linear-gradient(160deg,#e8e6e2,#b8aca0 55%,#3e2a22)" role="img" aria-label="Bedroom with dark wooden bed"></div><h3>BEDROOM</h3><div class="btn-more">MORE ›</div></article>
  <article class="category abs" style="left:224px"><div class="photo" style="background:linear-gradient(160deg,#c9a882,#8a5e38 55%,#d8c4a8)" role="img" aria-label="Living room with rattan sofas"></div><h3>LIVING ROOM</h3><div class="btn-more">MORE ›</div></article>
  <article class="category abs" style="left:368px"><div class="photo" style="background:linear-gradient(160deg,#e0d8cc,#5a3e30 50%,#2e1e18)" role="img" aria-label="Dining room with dark table and chairs"></div><h3>DINING ROOM</h3><div class="btn-more">MORE ›</div></article>
  <article class="category abs" style="left:513px"><div class="photo" style="background:linear-gradient(160deg,#dce8a0,#c8d070 50%,#8ab060)" role="img" aria-label="Bright kids room with yellow furniture"></div><h3>KIDS ROOMS</h3><div class="btn-more">MORE ›</div></article>
</section>

<div class="divider abs" style="top:1000px"></div>

<div class="brands abs">
  <span>Norvale</span><span>Beamcraft</span><span>lumo</span><span>Tallowfield</span><span>Quarrin</span><span>Birchway</span><span>Hartwell</span><span>Meadowlark</span>
</div>

<footer class="footer abs">
  <div class="fcol" style="left:86px;width:66px"><h4>Products</h4><ul><li>Bedroom</li><li>Living Room</li><li>Dining Room</li><li>Kids Rooms</li></ul></div>
  <div class="fcol" style="left:188px;width:80px"><h4>Information</h4><ul><li>Home</li><li>About Us</li><li>Blog</li><li>Contact us</li></ul></div>
  <div class="fcol" style="left:302px;width:80px"><h4>Your Account</h4><ul><li>Order Status</li><li>My Wishlist</li><li>Order History</li><li>Newsletter</li></ul></div>
  <div class="fcol" style="left:415px;width:117px"><h4>Newsletter Sign Up</h4><p>Lorem ipsudolor sit ec adipiscing elitsite amet</p><div class="email">Email Address</div><div class="btn-sub">SUBSCRIBE</div></div>
  <div class="fcol" style="left:570px;width:76px"><h4>Follow us</h4><ul class="social"><li><b></b>Chatterly</li><li><b></b>Peeplink</li><li><b></b>Circlenet</li></ul></div>
</footer>

<div class="bottom-bar abs">
  <span class="copy">© Copyright 2014 Oakmere Home. All Right Reserved</span>
  <div class="pay"><span>PayRun</span><span>CARDA</span><span>Orbit</span><span>Findex</span><span>Amexa</span></div>
</div>

</body>
</html>
```